Website Design for Varnel Ridge Holdings

I am looking to create a website with 3-4 pages for Varnel Ridge Holdings, a private investment holding company. We already have a logo created via PixelHarbor and would like to incorporate the same dark navy blue color scheme as well as white and potentially other colors including variants of blue, black, and white. We are looking for a conservative, polished design befitting a financial services firm. Our focus as a firm is on identifying opportunities in the overlooked - seeing opportunity where institutional investment is lacking. We are focused on building value for the long-term. We will provide virtually all of the text content but need assistance in setting up the layout, font, design, theme, graphics, etc. The initial three pages will be: Home Page / About Us, "Team", and "Portfolio". Right now, we do not have any portfolio companies but will likely have one within the next several months. The main content page will be the home page. The Team and Portfolio pages will be abbreviated. This website will be expository and is not primarily focused on lead generation or sales.

Ideally, we can incorporate some form of animations / transitions for titles and text sections and stock images (or ideally looped videos) of major city skylines in the U.S. , Latin America, and Europe as those regions are our core investment geographies.

Websites we like that you can use for references include many major private equity firms including Quarrystone Partners (https://www.quarrystonepartners.example/), Brightmoor (https://brightmoor.example/), KLV Holdings (https://www.klvholdings.example/), and Wexholm (https://www.wexholm.example/)
Updates

All,

Thank you to everyone who has posted the initial drafts of the Varnel Ridge Holdings website. The designs are very good. We would now like to review more refined drafts of our website from the designers.

We have posted updated, specific guidance on website page design and text. Please reference the new uploaded "Varnel Ridge Holdings Website Design Guidance" Microsoft Word document to refine your submissions.

Thank you!
Marcus

Target Market(s)

Investment Professionals

Industry/Entity Type

Financial Services

Coding

Coded - Design and coding required

Number of Pages Required

4 page

```html
<!DOCTYPE html>
<html lang="en">
<head>
<meta charset="utf-8">
<title>Varnel Ridge Holdings</title>
<link href="https://fonts.googleapis.com/css2?family=Michroma&family=Krona+One&family=Poppins:wght@400;500;600&family=Lato:wght@400;700&display=swap" rel="stylesheet">
<style>
:root{
  --navy:#0b1f4b;
  --navy-deep:#061a45;
  --orange:#f59e0b;
  --white:#ffffff;
  --pale:#f3f6fd;
  --grey:#7a7f8a;
  --line:#d9dce3;
  --red:#e5161b;
}
*{margin:0;padding:0;box-sizing:border-box}
html,body{width:1200px;height:3287px;overflow:hidden}
body{position:relative;background:var(--white);font-family:"Poppins",sans-serif;color:var(--navy)}
.abs{position:absolute}
.wide{font-family:"Michroma",sans-serif;font-weight:400}
.wide b{font-family:"Krona One",sans-serif;font-weight:400}
.center{text-align:center}

/* header */
.site-header{top:0;left:0;width:1200px;height:93px;background:var(--white)}
.brand{left:112px;top:28px;font-family:"Poppins",sans-serif;font-weight:600;font-size:30px;letter-spacing:3px;color:var(--navy);white-space:nowrap}
.nav a{position:absolute;top:36px;font-family:"Michroma",sans-serif;font-size:12px;color:var(--navy);text-decoration:none;letter-spacing:.5px}
.nav .active{font-family:"Krona One",sans-serif}
.btn{position:absolute;display:flex;align-items:center;justify-content:center;background:var(--navy);color:var(--white);font-family:"Krona One",sans-serif;font-size:13px;letter-spacing:.5px;text-decoration:none}
.btn-light{background:var(--white);color:var(--navy)}

/* hero */
.hero{top:93px;left:0;width:1200px;height:501px;background:linear-gradient(180deg,#4a4d6a 0%,#6d6478 35%,#5b5467 60%,#3a2f38 85%,#2a2530 100%)}
.hero-title{top:194px;left:0;width:1200px;color:var(--white);font-size:43px;line-height:62px}
.hero-sub{top:326px;left:200px;width:800px;color:var(--white);font-size:17px;line-height:28px}
.play{left:722px;top:407px}

/* about */
.about-title{top:668px;left:0;width:1200px;font-size:32px;line-height:47px}
.about-lead{top:778px;left:240px;width:720px;font-size:15.5px;line-height:27.5px}
.stat{top:900px;width:360px;text-align:center}
.stat-num{font-family:"Poppins",sans-serif;font-weight:600;font-size:50px;line-height:60px;color:var(--orange)}
.stat-label{font-weight:500;font-size:17px;margin-top:2px}
.about-photo{left:111px;top:1053px;width:489px;height:419px;background:linear-gradient(135deg,#9fb0c4,#5b6b80 55%,#c9b49a)}
.about-copy{left:674px;top:1044px;width:414px;font-size:15.5px;line-height:27.5px;text-align:justify}
.about-copy p+p{margin-top:27.5px}

/* team */
.team{top:1579px;left:0;width:1200px;height:552px;background:var(--pale)}
.team-title{top:1642px;left:0;width:1200px;font-size:32px}
.card{top:1714px;width:221px;height:331px;background:var(--white);border-radius:6px;box-shadow:0 2px 10px rgba(11,31,75,.08);text-align:center;font-family:"Lato",sans-serif}
.avatar{width:86px;height:86px;border-radius:50%;margin:30px auto 0;background:linear-gradient(160deg,#8c7a6c,#2e2b32)}
.card h3{font-family:"Poppins",sans-serif;font-weight:600;font-size:17px;margin-top:22px;letter-spacing:.3px}
.card .role{font-size:15px;margin-top:4px;color:var(--navy)}
.card .bio{font-size:13.5px;line-height:24px;color:var(--grey);margin:8px 10px 0}
.socials{display:flex;justify-content:center;gap:6px;margin-top:12px}
.socials span{width:24px;height:24px;border:1px solid #9aa0ab;border-radius:50%}

/* steps */
.steps-title{top:2198px;left:0;width:1200px;font-size:32px;line-height:47px}
.steps-lead{top:2303px;left:240px;width:720px;font-size:15.5px;line-height:28px}
.step{top:2388px;width:244px}
.step-num{font-family:"Poppins",sans-serif;font-weight:600;font-size:14px;color:var(--orange);padding-left:4px}
.step hr{border:0;border-top:1px solid var(--line);margin:12px 0 10px}
.step h4{font-weight:400;font-size:15.5px;line-height:24px}
.step p{font-size:13px;line-height:23px;margin-top:6px;color:#3a4560}

/* contact */
.contact{top:2630px;left:0;width:1200px;height:397px;background:var(--white)}
.contact-photo{top:2630px;left:0;width:664px;height:397px;background:linear-gradient(90deg,#b9b2a6 0%,#8a8f9c 40%,#d5d6da 80%,#ffffff 100%)}
.contact-title{top:2672px;left:723px;font-size:31px;line-height:48px}
.contact-copy{top:2771px;left:723px;width:365px;font-size:15.5px;line-height:25.7px;text-align:justify}

/* footer */
.site-footer{top:3027px;left:0;width:1200px;height:260px;background:var(--navy-deep);color:var(--white)}
.footer-brand{left:112px;top:3105px;font-weight:600;font-size:30px;letter-spacing:3px;color:var(--white);white-space:nowrap}
.copyright{left:111px;top:3173px;font-size:15.5px;color:var(--white)}
.fcol{top:3095px;color:var(--white)}
.fcol h5{font-family:"Krona One",sans-serif;font-weight:400;font-size:15px;margin-bottom:14px}
.fcol li{list-style:none;font-size:15.5px;line-height:33px}
</style>
</head>
<body>

<header class="site-header abs">
  <div class="brand abs">VARNEL RIDGE HOLDINGS</div>
  <nav class="nav">
    <a class="active" style="left:620px" href="#">HOME</a>
    <a style="left:724px" href="#">TEAM</a>
    <a style="left:823px" href="#">PORTFOLIO</a>
  </nav>
  <a class="btn" style="left:959px;top:24px;width:129px;height:42px;font-size:11.5px;font-family:'Michroma',sans-serif" href="#">CONTACT US</a>
</header>

<section class="hero abs" role="img" aria-label="City skyline at dusk with office towers and waterfront"></section>
<h1 class="hero-title abs wide center">WE SEE OPPORTUNITY <b>WHERE</b><br><b>OTHERS OVERLOOK</b></h1>
<p class="hero-sub abs center">Varnel Ridge Holdings is a private investment holding company focused on long-term value creation in underserved markets.</p>
<a class="btn btn-light" style="left:421px;top:406px;width:268px;height:50px" href="#">EXPLORE OUR APPROACH</a>
<svg class="play abs" width="46" height="46" viewBox="0 0 46 46" aria-hidden="true"><circle cx="23" cy="23" r="23" fill="var(--red)"/><path d="M18 14 L32 23 L18 32 Z" fill="#fff"/></svg>

<h2 class="about-title abs wide center">ABOUT<br><b>VARNEL RIDGE HOLDINGS</b></h2>
<p class="about-lead abs center">Lorem ipsum dolor sit amet, consectetur adipiscing elit, sed do eiusmod tempor incididunt ut labore et dolore magna aliqua. Ut enim ad minim veniam, quis nostrud exercitation ullamco laboris nisi ut aliquip ex ea commodo consequat.</p>

<div class="stat abs" style="left:37px"><div class="stat-num">$73bn</div><div class="stat-label">Excepteur sint occaecat</div></div>
<div class="stat abs" style="left:420px"><div class="stat-num">300+</div><div class="stat-label">Duis aute</div></div>
<div class="stat abs" style="left:785px"><div class="stat-num">80+</div><div class="stat-label">Deserunt mollit anim id est</div></div>

<div class="about-photo abs" role="img" aria-label="Colleagues in a bright office meeting around a table with laptops"></div>
<div class="about-copy abs">
  <p>Lorem ipsum dolor sit amet, consectetur adipiscing elit, sed do eiusmod tempor incididunt ut labore et dolore magna aliqua. Ut enim ad minim veniam, quis nostrud exercitation ullamco laboris nisi ut aliquip ex ea comm odo consequat. Duis aute irure dolor in reprehenderit in voluptate velit esse cillum dolore eu fugiat nulla pariaur. Excepteur sint occaecat cupidatat non proident, sunt in culpa qui officia deserunt mollit anim id est laborum.</p>
  <p>Nemo enim ipsam voluptatem quia voluptas sit aspernatur aut odit aut fugit, sed quia consequuntur magni dolores eos qui ratione voluptatem.</p>
</div>
<a class="btn" style="left:674px;top:1421px;width:148px;height:51px" href="#">READ MORE</a>

<section class="team abs"></section>
<h2 class="team-title abs wide center">OUR <b>TEAM</b></h2>

<article class="card abs" style="left:110px">
  <div class="avatar" role="img" aria-label="Portrait photo of team member"></div>
  <h3>OWEN HALE</h3><div class="role">Founder</div>
  <p class="bio">Sed ut perspiciatis unde omnis iste natus er ror sit voluptatem accusantium dolorea.</p>
  <div class="socials"><span></span><span></span><span></span></div>
</article>
<article class="card abs" style="left:361px">
  <div class="avatar" role="img" aria-label="Portrait photo of team member"></div>
  <h3>DORIAN VASK</h3><div class="role">Founder</div>
  <p class="bio">Itaque earum rerum hic tenetur a sapiente delectus, ut aut reiciendis voluptatibus</p>
  <div class="socials"><span></span><span></span><span></span></div>
</article>
<article class="card abs" style="left:613px">
  <div class="avatar" role="img" aria-label="Portrait photo of team member"></div>
  <h3>LENA CORVO</h3><div class="role">Founder</div>
  <p class="bio">Sed ut perspiciatis unde omnis iste natus er ror sit volupta tem accusantium</p>
  <div class="socials"><span></span><span></span><span></span></div>
</article>
<article class="card abs" style="left:864px">
  <div class="avatar" role="img" aria-label="Portrait photo of team member"></div>
  <h3>DORIAN VASK</h3><div class="role">Founder</div>
  <p class="bio">Earum rerum hic tenetur a sapiente delectus, ut aut reiciendis voluptatibus</p>
  <div class="socials"><span></span><span></span><span></span></div>
</article>

<h2 class="steps-title abs wide center">EXCEPTEUR SINT OCCAECAT <b>CUPID</b><br><b>ATAT NON PROIDENT</b></h2>
<p class="steps-lead abs center">Lorem ipsum dolor sit amet, consectetur adipiscing elit, sed do eiusmod tempor incididunt ut labore et llamco laboris nisi ut aliquip ex ea commodo consequat.</p>

<div class="step abs" style="left:73px"><div class="step-num">01</div><hr><h4>Duis aute irure dolor in reprehenderit</h4><p>Excepteur sint occaecat cupidatat non proident, sunt in culpa qui officia deserunt mollit anim id est</p></div>
<div class="step abs" style="left:343px"><div class="step-num">02</div><hr><h4>Duis aute irure dolor in reprehenderit</h4><p>Excepteur sint occaecat cupidatat non proident, sunt in culpa qui officia deserunt mollit anim id est</p></div>
<div class="step abs" style="left:614px"><div class="step-num">03</div><hr><h4>Duis aute irure dolor in reprehenderit</h4><p>Excepteur sint occaecat cupidatat non proident, sunt in culpa qui officia deserunt mollit anim id est</p></div>
<div class="step abs" style="left:883px"><div class="step-num">04</div><hr><h4>Duis aute irure dolor in reprehenderit</h4><p>Excepteur sint occaecat cupidatat non proident, sunt in culpa qui officia deserunt mollit anim id est</p></div>

<section class="contact abs"></section>
<div class="contact-photo abs" role="img" aria-label="Three smiling colleagues gathered around a laptop"></div>
<h2 class="contact-title abs wide">GET IN TOUCH<br><b>WITH US</b></h2>
<p class="contact-copy abs">Duis aute irure dolor in reprehenderit in volupt ate velit esse cillum dolore eu fugiat nulla pariatur. Excepteur sint occaecat cupidatat non proident, sunt in culpa qui officia deserunt mollit anim id est laborum.</p>
<a class="btn" style="left:723px;top:2918px;width:175px;height:50px" href="#">GET STARTED</a>

<footer class="site-footer abs"></footer>
<div class="footer-brand abs">VARNEL RIDGE HOLDINGS</div>
<p class="copyright abs">Copyrights@2025.Varnel Ridge.All Rights Reserved</p>
<div class="fcol abs" style="left:583px">
  <h5>QUICK LINKS</h5>
  <ul><li>Home</li><li>Team</li><li>Portfolio</li></ul>
</div>
<div class="fcol abs" style="left:771px">
  <h5>CONTACT US</h5>
  <ul><li>Varnel Ridge Holdings, United States</li><li>+1 555 014 2290</li><li>info@varnelridgeholdings.example</li></ul>
</div>

</body>
</html>
```